Premium Coffee Business Needs a Wordpress Design

We need a Wordpress design for a Premium Coffee E-commerce based in Sao Paulo, Brazil. We want something very similar to tallowfinchroasters.com, but with a few exceptions, better described in the attachment (PLEASE READ our specifications). The product we're selling is premium, so we need to communicate sophistication, and at the same time people should feel they're in contact with an innovative company. Our company is called Coffee Meridian.
Adults aged 25 to 50 who have refined tastes.
Business

```html
<!DOCTYPE html>
<html lang="en">
<head>
<meta charset="utf-8">
<title>Premium Coffee</title>
<link href="https://fonts.googleapis.com/css2?family=Rokkitt:wght@400;500;700&family=Josefin+Slab:wght@400;600&family=Arimo:wght@400;700&display=swap" rel="stylesheet">
<style>
:root{
  --espresso:#2a1210;
  --espresso-mid:#3d1c18;
  --crimson:#d02a1a;
  --crimson-dark:#a61c10;
  --ink:#2b1a16;
  --paper:#ffffff;
  --field:#f0eeec;
  --footer:#222222;
  --footer-strip:#303030;
  --footer-text:#ffffff;
}
*{margin:0;padding:0;box-sizing:border-box}
html,body{width:1200px;height:1166px;overflow:hidden}
body{position:relative;font-family:"Josefin Slab",serif;color:var(--ink)}
.backdrop{position:absolute;inset:0;background:radial-gradient(ellipse at 85% 40%,#f4f1ee 0%,#e6dfda 35%,#cdbdb3 70%,#b9a89c 100%)}
.brand{position:absolute;left:155px;top:30px;font-family:"Rokkitt",serif;font-weight:700;font-size:46px;color:var(--espresso);letter-spacing:.5px}
.search{position:absolute;left:725px;top:41px;display:flex;height:35px}
.search input{width:235px;border:1px solid #d0ccc8;background:var(--field);font-family:Arimo,sans-serif;font-size:14px;padding:0 11px;color:#999}
.search button{width:82px;border:0;background:var(--crimson);color:#fff;font-family:Arimo,sans-serif;font-size:16px}
.sheet{position:absolute;left:157px;top:104px;width:886px;height:954px;background:var(--paper)}
.ribbon-tail{position:absolute;top:122px;width:34px;height:58px;background:var(--crimson-dark)}
.ribbon-tail.left{left:98px;clip-path:polygon(0 100%,30% 0,100% 0,100% 100%)}
.ribbon-tail.right{left:1068px;clip-path:polygon(0 0,70% 0,100% 100%,0 100%)}
.nav{position:absolute;left:129px;top:115px;width:942px;height:53px;background:linear-gradient(#4a2420,var(--espresso));border-bottom:1px solid #8a3a2c;display:flex;align-items:center;padding-left:32px}
.nav a{font-family:"Rokkitt",serif;font-size:17px;color:#fff;text-decoration:none;text-transform:uppercase}
.hero{position:absolute;left:157px;top:174px;width:886px;height:370px;background:linear-gradient(100deg,#7a5a44 0%,#e8e2dc 35%,#cfc5bc 50%,#4a2a1a 70%,#c9b9a6 100%)}
.about h1{position:absolute;left:177px;top:562px;font-family:"Rokkitt",serif;font-weight:500;font-size:44px;letter-spacing:1.5px;color:var(--espresso)}
.about h1 span{color:var(--crimson)}
.about p{position:absolute;left:177px;width:836px;font-size:14.4px;line-height:20.3px;text-align:justify;color:#1d1411}
.feature{position:absolute;top:821px;width:270px;height:210px}
.feature .tab{position:absolute;left:86px;top:0;width:114px;height:62px;background:var(--espresso);border-radius:57px 57px 0 0}
.feature .tab svg{position:absolute;left:37px;top:10px}
.feature .frame{position:absolute;left:0;top:60px;width:270px;height:150px;border:5px solid var(--espresso)}
.feature .photo{width:100%;height:100%}
.footer{position:absolute;left:0;top:1058px;width:1200px;height:108px;background:var(--footer)}
.footer-links{position:absolute;left:0;top:14px;width:1200px;height:34px;background:var(--footer-strip);display:flex;align-items:center;padding-left:171px;font-family:Arimo,sans-serif;font-weight:700;font-size:14px;color:var(--footer-text)}
.footer-links .sep{margin:0 21px}
.social{position:absolute;left:958px;top:9px;display:flex;gap:10px}
.social span{width:15px;height:15px;border-radius:50%;background:#9a9a9a}
.signup{position:absolute;left:173px;top:59px;display:flex;gap:8px}
.signup input{width:239px;height:35px;border:0;border-radius:3px;background:#e6e2df}
.signup button{width:72px;height:35px;border:0;border-radius:3px;background:var(--crimson);color:#fff;font-family:Arimo,sans-serif;font-weight:700;font-size:14px}
.legal{position:absolute;left:556px;top:74px;font-family:Arimo,sans-serif;font-weight:700;font-size:12px;color:#e8e8e8}
</style>
</head>
<body>
<div class="backdrop" role="img" aria-label="Soft blurred photo of a coffee cup and scattered beans"></div>

<div class="brand">Premium Coffee</div>
<form class="search"><input type="text" value="search keyword"><button type="button">Search</button></form>

<div class="sheet"></div>
<div class="ribbon-tail left"></div>
<div class="ribbon-tail right"></div>
<nav class="nav">
  <a style="margin-right:65px">Home</a>
  <a style="margin-right:65px">Brewing Guides</a>
  <a style="margin-right:71px">Subscriptions</a>
  <a style="margin-right:71px">Merchandise</a>
  <a style="margin-right:59px">Blog</a>
  <a>Our Story</a>
</nav>

<div class="hero" role="img" aria-label="Steaming cup of coffee on a saucer beside a burlap sack of roasted beans on a wooden table"></div>

<section class="about">
  <h1><span>About</span> Premium Coffee</h1>
  <p style="top:627px">Lorem Ipsum is simply dummy text of the printing and typesetting industry. Lorem Ipsum has been the industry's standard dummy text ever since the 1500s, when an unknown printer took a galley of type and scrambled it to make a type specimen book. It has survived not only five centuries text of the printing and typesetting industry. Lorem Ipsum has been the industry's standard dummy text ever since the 1500s, when an unknown printer took a galley of type and scrambled.</p>
  <p style="top:728px">Lorem Ipsum has been the industry's standard dummy text ever since the 1500s, when an unknown printer took a galley of type and scrambled it to make a type specimen book. It has survived not only five centuries.</p>
</section>

<div class="feature" style="left:171px">
  <div class="tab"><svg width="40" height="40" viewBox="0 0 40 40"><circle cx="20" cy="20" r="15" fill="none" stroke="#fff" stroke-width="3"/><path d="M20 20 L20 5 M20 20 L33 27 M20 20 L7 27" stroke="#fff" stroke-width="2"/><circle cx="15" cy="14" r="2" fill="#fff"/><circle cx="26" cy="15" r="2" fill="#fff"/><circle cx="20" cy="29" r="2" fill="#fff"/></svg></div>
  <div class="frame"><div class="photo" role="img" aria-label="Assorted iced and hot coffee drinks with latte art and roasted beans" style="background:linear-gradient(110deg,#e9e3dc,#a86a3c 40%,#d9a56a 60%,#4a2a1a 85%)"></div></div>
</div>
<div class="feature" style="left:464px">
  <div class="tab"><svg width="40" height="40" viewBox="0 0 40 40"><path d="M6 28 A14 14 0 0 1 34 28 Z" fill="#fff"/><rect x="3" y="30" width="34" height="3" fill="#fff"/><circle cx="20" cy="12" r="2.5" fill="#fff"/></svg></div>
  <div class="frame"><div class="photo" role="img" aria-label="Cup of black coffee surrounded by roasted beans and a burlap sack" style="background:linear-gradient(100deg,#b89a70,#f2f0ee 35%,#2a1810 50%,#6a4226 75%,#b89a70)"></div></div>
</div>
<div class="feature" style="left:757px">
  <div class="tab"><svg width="40" height="40" viewBox="0 0 40 40"><circle cx="20" cy="8" r="3" fill="#fff"/><path d="M8 19 A12 9 0 0 1 32 19 Z" fill="#fff"/><path d="M9 21 H31 L28 36 H12 Z" fill="#fff"/><path d="M14 22 V35 M18 22 V35 M22 22 V35 M26 22 V35" stroke="#2a1210" stroke-width="1.2"/></svg></div>
  <div class="frame"><div class="photo" role="img" aria-label="Cappuccino dusted with cocoa on a saucer beside a biscuit and a menu" style="background:linear-gradient(100deg,#3a3a3a,#d8d8d8 30%,#f4f2ef 50%,#b06a40 65%,#e8e4e0 85%)"></div></div>
</div>

<footer class="footer">
  <div class="footer-links">
    <span>Contact</span><span class="sep">|</span><span>Special Orders</span><span class="sep">|</span><span>Wholesale</span><span class="sep">|</span><span>Press</span><span class="sep">|</span><span>FAQ</span>
    <div class="social"><span></span><span></span><span></span></div>
  </div>
  <form class="signup"><input type="text" aria-label="Email address"><button type="button">Sign Up</button></form>
  <div class="legal">Shipping and Returns Terms of Use Privacy © 2013 Tallowfinch Roasters Inc., All Rights Reserved</div>
</footer>
</body>
</html>
```